BUSINESS CARD

Design Creative Business Card

Vellomar (see attached company logo)
Online Analytics | Data Science

Rodrigo Emil Bárcena Lutfi (CEO)
Data Science

(high quality logo, and two other names will be provided)

UPDATE:
- no black background please. Use a nice blue tone that symbolizes trust, along with the green of the vellomar company logo.

```html
<!DOCTYPE html>
<html lang="en">
<head>
<meta charset="utf-8">
<title>Vellomar Business Card</title>
<link rel="stylesheet" href="https://fonts.googleapis.com/css2?family=Tinos:wght@400;700&display=swap">
<style>
  :root {
    --page-bg: #ecebe8;
    --card-white: #ffffff;
    --trust-blue: #3b63c9;
    --trust-blue-deep: #2647a8;
    --trust-blue-light: #5b82e0;
    --name-blue: #1f3a8f;
    --ink: #2e3236;
    --ink-soft: #3d3d3d;
    --band-line: #3a3d40;
    --accent-grey: #d9dbdc;
  }
  * { box-sizing: border-box; margin: 0; padding: 0; }
  html, body {
    width: 1200px; height: 1200px; overflow: hidden;
    background: var(--page-bg);
  }
  .canvas { position: relative; width: 1200px; height: 1200px; }

  .card {
    position: absolute;
    width: 627px; height: 345px;
    background: var(--card-white);
    box-shadow: 0 6px 14px rgba(0,0,0,0.28);
    overflow: hidden;
    font-family: "Tinos", "Times New Roman", serif;
  }
  .card svg.card-art { position: absolute; inset: 0; }

  .card-front { left: 244px; top: 169px; }
  .card-back  { left: 257px; top: 696px; }

  .contact {
    position: absolute; right: 14px; top: 14px;
    text-align: right; color: var(--ink-soft);
    font-size: 13px; line-height: 18px;
  }
  .contact .person-name {
    color: var(--name-blue); font-size: 20px; line-height: 24px;
    margin-bottom: 2px;
  }
  .contact .line { display: flex; justify-content: flex-end; align-items: center; gap: 5px; }
  .contact .line svg { width: 12px; height: 12px; }

  .website {
    position: absolute; right: 14px; bottom: 14px;
    font-size: 27px; font-weight: 700; color: var(--ink);
    text-shadow: 0 2px 3px rgba(0,0,0,0.25);
  }
  .mark-spot {
    position: absolute; left: 290px; top: 90px;
    width: 170px; height: 170px; border-radius: 50%;
    background: var(--accent-grey); opacity: 0.45;
  }

  .brand {
    position: absolute; left: 0; right: 0; top: 132px;
    text-align: center;
    font-size: 66px; font-weight: 700; color: var(--ink);
    letter-spacing: 1px;
  }
</style>
</head>
<body>
<main class="canvas">

  <section class="card card-front" aria-label="Business card front">
    <svg class="card-art" width="627" height="345" viewBox="0 0 627 345">
      <defs>
        <linearGradient id="frontBlue" x1="0" y1="0" x2="1" y2="0">
          <stop offset="0" stop-color="var(--trust-blue-deep)"/>
          <stop offset="0.45" stop-color="var(--trust-blue-light)"/>
          <stop offset="1" stop-color="var(--trust-blue)"/>
        </linearGradient>
        <filter id="curveShadow" x="-20%" y="-20%" width="140%" height="140%">
          <feGaussianBlur stdDeviation="5"/>
        </filter>
      </defs>
      <path d="M283 0 C232 120 172 250 146 345" fill="none" stroke="#000" stroke-opacity="0.35" stroke-width="10" filter="url(#curveShadow)"/>
      <path class="side-panel" d="M0 0 H283 C232 120 172 250 146 345 H0 Z" fill="url(#frontBlue)"/>
    </svg>

    <div class="mark-spot" aria-hidden="true"></div>

    <div class="contact">
      <p class="person-name">Rodrigo Emil Bárcena Lutfi</p>
      <p>CEO</p>
      <p>Data Science</p>
      <p class="line">
        <svg viewBox="0 0 12 12" aria-hidden="true"><rect x="1" y="2.5" width="10" height="7" fill="#333"/><path d="M1 2.5 L6 6.5 L11 2.5" fill="none" stroke="#fff" stroke-width="1"/></svg>
        emil@vellomar.com
      </p>
      <p class="line">
        <svg viewBox="0 0 12 12" aria-hidden="true"><path d="M2 4 Q6 0 10 4 L9 5.5 L7.5 4.5 L4.5 4.5 L3 5.5 Z" fill="#333"/><rect x="3" y="6" width="6" height="4.5" rx="1" fill="#333"/></svg>
        555-014-2290 EXT. 114
      </p>
    </div>

    <p class="website">www.vellomar.com</p>
  </section>

  <section class="card card-back" aria-label="Business card back">
    <svg class="card-art" width="627" height="345" viewBox="0 0 627 345">
      <defs>
        <linearGradient id="backBlue" x1="0" y1="0" x2="1" y2="1">
          <stop offset="0" stop-color="var(--trust-blue-deep)"/>
          <stop offset="0.5" stop-color="var(--trust-blue-light)"/>
          <stop offset="1" stop-color="var(--trust-blue)"/>
        </linearGradient>
      </defs>
      <rect width="627" height="345" fill="url(#backBlue)"/>
      <path class="white-band" d="M0 152 C110 62 400 26 627 32 L627 212 C520 292 250 318 0 302 Z" fill="var(--card-white)"/>
      <path d="M0 152 C110 62 400 26 627 32" fill="none" stroke="var(--band-line)" stroke-width="5"/>
      <path d="M627 212 C520 292 250 318 0 302" fill="none" stroke="var(--band-line)" stroke-width="5"/>
    </svg>
    <p class="brand">vellomar.com</p>
  </section>

</main>
</body>
</html>
```